JT & WE Shearing Pty Ltd

We already have an existing logo created by Lumen Quarry however we have restructured to a company. We would like someone to add Pty Ltd to our business name please.

Colors

Designer to choose only greyscale colors for use in the design.

```html
<!DOCTYPE html>
<html lang="en">
<head>
<meta charset="utf-8">
<title>JT &amp; WE Shearing Pty Ltd – Business Card</title>
<link rel="stylesheet" href="https://fonts.googleapis.com/css2?family=Lato:wght@400;700&display=swap">
<style>
  :root {
    --card-black: #050608;
    --ink-white: #ffffff;
    --icon-ink: #050608;
  }
  html, body {
    margin: 0;
    padding: 0;
    width: 1200px;
    height: 750px;
    overflow: hidden;
    background: var(--card-black);
  }
  .business-card {
    position: relative;
    width: 1200px;
    height: 750px;
    overflow: hidden;
    background: var(--card-black);
    color: var(--ink-white);
    font-family: "Lato", sans-serif;
  }
  .wordmark {
    margin: 0;
    font-family: "Lato", sans-serif;
    font-weight: 700;
    color: var(--ink-white);
  }
  .wordmark__name,
  .wordmark__descriptor {
    position: absolute;
    left: 392px;
    width: 702px;
    text-align: center;
    white-space: nowrap;
    line-height: 1;
  }
  .wordmark__name {
    top: 108px;
    font-size: 180px;
    letter-spacing: 2px;
  }
  .wordmark__descriptor {
    top: 300px;
    font-size: 70px;
    letter-spacing: 0;
  }
  .contact-list {
    position: absolute;
    left: 61px;
    top: 496px;
    margin: 0;
    padding: 0;
    list-style: none;
  }
  .contact-item {
    display: flex;
    align-items: center;
    height: 56px;
    margin-bottom: 21px;
    font-size: 37px;
    font-weight: 400;
    white-space: nowrap;
  }
  .contact-item__icon {
    width: 48px;
    height: 48px;
    margin-right: 32px;
    flex: none;
  }
</style>
</head>
<body>
  <main class="business-card">
    <h1 class="wordmark">
      <span class="wordmark__name">JT &amp; WE</span>
      <span class="wordmark__descriptor">SHEARING PTY LTD</span>
    </h1>

    <ul class="contact-list">
      <li class="contact-item">
        <svg class="contact-item__icon" viewBox="0 0 48 48" aria-hidden="true">
          <circle cx="24" cy="24" r="24" fill="var(--ink-white)"/>
          <path d="M24 10c-6 0-10.5 4.6-10.5 10.4C13.5 28 24 38 24 38s10.5-10 10.5-17.6C34.5 14.6 30 10 24 10z" fill="var(--icon-ink)"/>
          <circle cx="24" cy="20.5" r="4" fill="var(--ink-white)"/>
        </svg>
        <span class="contact-item__text">PO Box 418 YORKDALE WA 6399</span>
      </li>
      <li class="contact-item">
        <svg class="contact-item__icon" viewBox="0 0 48 48" aria-hidden="true">
          <circle cx="24" cy="24" r="24" fill="var(--ink-white)"/>
          <path d="M16.5 11.5c1-.8 2.4-.6 3.1.4l3 4.3c.6.9.5 2.1-.3 2.8l-2 1.8c1.4 3 3.8 5.6 6.8 7.2l1.900-1.9c.8-.7 2-.8 2.8-.2l4.3 3c1 .7 1.2 2.1.4 3.1l-2 2.4c-1 1.2-2.7 1.6-4.2 1.1C21.7 33 15 26.3 12.5 17.8c-.5-1.5 0-3.1 1.1-4.1z" fill="var(--icon-ink)"/>
        </svg>
        <span class="contact-item__text">Ray 0491570156</span>
      </li>
      <li class="contact-item">
        <svg class="contact-item__icon" viewBox="0 0 48 48" aria-hidden="true">
          <circle cx="24" cy="24" r="24" fill="var(--ink-white)"/>
          <rect x="13" y="16" width="22" height="16" rx="1.5" fill="var(--icon-ink)"/>
          <path d="M14 17.5l10 8 10-8M14 30.5l7.5-6.5M34 30.5l-7.5-6.5" stroke="var(--ink-white)" stroke-width="1.6" fill="none"/>
        </svg>
        <span class="contact-item__text">jtweshearing@fieldpost.com</span>
      </li>
    </ul>
  </main>
</body>
</html>
```